ALL TEXT GRAPHICS TM May 2025 for Instagram

We are looking for a series of social media graphics for Instagram (new size: 4:5 (1080 x 1350 pixels) ratio that are ALL TEXT. We want the following quotes below on each graphic; one quote per graphic. AND, In very small letters at the bottom of each graphic, add @TovaMarshOnline
The look and feel of these graphics should be complimentary to the color palette attached below; but keep them simple. But the design is up to you; at the end of this document, I provided various samples of all text graphics that I like as examples.
Target Market(s)
women looking to lose weight
Look and feel

```html
<!DOCTYPE html>
<html lang="en">
<head>
<meta charset="utf-8">
<title>All Text Graphics – TM May 2025</title>
<link href="https://fonts.googleapis.com/css2?family=Cinzel:wght@400&family=Roboto:wght@700&display=swap" rel="stylesheet">
<style>
  :root {
    --backdrop: #a9a9a9;
    --card: #ffffff;
    --headline: #c4005e;
    --accent: #e8007f;
    --ink: #1a1a1a;
  }
  * { margin: 0; padding: 0; box-sizing: border-box; }
  html, body { width: 1200px; height: 2957px; overflow: hidden; background: var(--backdrop); }
  .board { position: relative; width: 1200px; height: 2957px; }
  .post {
    position: absolute; width: 437px; height: 547px; background: var(--card);
    padding: 0 30px 0 38px;
  }
  .col-a { left: 156px; }
  .col-b { left: 607px; }
  .row-1 { top: 88px; }
  .row-2 { top: 648px; }
  .row-3 { top: 1206px; }
  .row-4 { top: 1765px; }
  .row-5 { top: 2323px; }
  .copy { position: absolute; left: 38px; right: 20px; }
  .headline {
    font-family: "Roboto", sans-serif; font-weight: 700; color: var(--headline);
    font-size: 40px; line-height: 1.18; margin-bottom: 12px;
  }
  .statement {
    font-family: "Cinzel", serif; font-weight: 400; color: var(--ink);
    font-size: 38px; line-height: 1.26; margin-bottom: 12px;
  }
  .callout {
    font-family: "Roboto", sans-serif; font-weight: 700; color: var(--accent);
    font-size: 38px; line-height: 1.2;
  }
  .handle {
    position: absolute; left: 40px; top: 473px;
    font-family: "Roboto", sans-serif; font-weight: 700; font-size: 14px; color: var(--ink);
  }
</style>
</head>
<body>
<main class="board">

  <article class="post col-a row-1">
    <div class="copy" style="top:78px">
      <h2 class="headline">Tired. Moody.<br>Stubborn Belly Fat.</h2>
      <p class="statement">Your hormones are screaming for help!</p>
      <p class="callout">Let’s fix that.</p>
    </div>
    <span class="handle">@TovaMarshOnline</span>
  </article>

  <article class="post col-b row-1">
    <div class="copy" style="top:70px">
      <h2 class="headline" style="font-size:37px">That stubborn weight?<br>It’s not your fault.</h2>
      <p class="statement">Your hormones are to blame and you’re not alone;</p>
      <p class="callout" style="font-size:36px">But there is a fix.</p>
    </div>
    <span class="handle">@TovaMarshOnline</span>
  </article>

  <article class="post col-a row-2">
    <div class="copy" style="top:78px">
      <h2 class="headline">Your belly isn’t fat…<br>it’s hormonal.</h2>
      <p class="statement">And here’s how to fix it.</p>
      <p class="callout" style="font-size:35px">Comment HORMONES if nothing is working.</p>
    </div>
    <span class="handle">@TovaMarshOnline</span>
  </article>

  <article class="post col-b row-2">
    <div class="copy" style="top:60px">
      <h2 class="headline" style="font-size:37px">The stubborn belly<br>fat after 40?</h2>
      <p class="statement" style="font-size:46px;line-height:1.17">It’s not about calories; it’s about your hormones.</p>
      <p class="callout">Here is the fix!</p>
    </div>
    <span class="handle">@TovaMarshOnline</span>
  </article>

  <article class="post col-a row-3">
    <div class="copy" style="top:96px;left:34px">
      <h2 class="headline" style="font-size:37px">Flat tummy in your<br>40s? It’s still possible!</h2>
      <p class="statement">Comment bye belly to get the 10 secrets to a flatter tummy</p>
    </div>
    <span class="handle" style="left:36px">@TovaMarshOnline</span>
  </article>

  <article class="post col-b row-3">
    <div class="copy" style="top:58px;left:36px">
      <h2 class="headline" style="font-size:37px">Bloating. Muffin top.<br>Puffy waistline.</h2>
      <p class="statement" style="font-size:45px;line-height:1.17">Your body’s screaming for a different kind of fix.</p>
      <p class="callout">Here it is</p>
    </div>
    <span class="handle" style="left:38px">@TovaMarshOnline</span>
  </article>

  <article class="post col-a row-4">
    <div class="copy" style="top:60px;left:50px">
      <h2 class="headline" style="font-size:37px;line-height:1.1">You’re<br>doing all the “right” things, but your belly won’t go down?</h2>
      <p class="statement" style="font-size:50px;line-height:1.14">Here’s what you haven’t tried.</p>
    </div>
    <span class="handle" style="left:51px">@TovaMarshOnline</span>
  </article>

  <article class="post col-b row-4">
    <div class="copy" style="top:54px">
      <h2 class="headline" style="font-size:37px">This 90-day<br>plan helped women over 40 slim down,</h2>
      <p class="statement" style="font-size:46px;line-height:1.18">Get a tiny waist and feel sexy again.</p>
      <p class="callout">You’re next.</p>
    </div>
    <span class="handle">@TovaMarshOnline</span>
  </article>

  <article class="post col-a row-5">
    <div class="copy" style="top:58px;left:43px">
      <h2 class="headline">This is the secret<br>women over 40</h2>
      <p class="statement" style="font-size:36px;line-height:1.22">Are using to get snatched without starving. Comment skinny to get the exact plan.</p>
    </div>
    <span class="handle" style="left:45px">@TovaMarshOnline</span>
  </article>

  <article class="post col-b row-5">
    <div class="copy" style="top:66px;left:37px">
      <h2 class="headline" style="font-size:37px">What worked in your<br>30s won’t work now.</h2>
      <p class="statement" style="font-size:46px;line-height:1.17">Here’s what actually does.</p>
      <p class="callout">Drop 30 Pounds in<br>3 Months.</p>
    </div>
    <span class="handle" style="left:39px">@TovaMarshOnline</span>
  </article>

</main>
</body>
</html>
```